Newsletter (nur grafisch) Kreditvermittlung Alu-Kasse
Kreditsuchende stellen bei uns EINEN Kreditantrag und wir verhandeln mit bis zu 20 Banken und präsentieren dem Kunden dann das beste Angebot absolut kostenlos und unverbindlich.
Spezielle Landingpage:
www.alu-kasse-muster.de/kredit.htm
Wir wollen eine Newslettervorlage, die dieses Angebot bewirbt. Wir brauchen nur das Design - die Umsetzung in html können wir dann selbst.
Die notwendigen Bilddateien müssen vom Gewinner zur Verfügung gestellt werden.
Skizzenhafte Ausführung bei Dingen, die klar sind (z.B. Header) genügen.
Text kann Fülltext verwendet werden oder Sie schreiben schnell eine Kleinigkeit, inspiriert durch die Landingpage.
Wir sind mittlerweile betriebsblind und für jeden frischen Wind dankbar!
Langfristige Zusammenarbeit:
Wir benötigen ständig Grafiken, Werbemittel und html-Arbeiten. Der Gewinner dieses Wettbewerbs kann sich auf weitere lukrative Aufträge freuen!

```html
<!DOCTYPE html>
<html lang="de">
<head>
<meta charset="utf-8">
<title>Alu-Kasse Newsletter</title>
<link rel="stylesheet" href="https://fonts.googleapis.com/css2?family=Arimo:wght@400;700&display=swap">
<style>
  :root {
    --bg-top: #e6e8f4;
    --bg-top-edge: #d6d9ea;
    --bg-bottom-a: #b8cce2;
    --bg-bottom-b: #d6e4f4;
    --teal-dark: #003f4e;
    --teal-text: #00424f;
    --card: #ffffff;
    --text: #1a1a1a;
    --rule: #e3e6ea;
    --tick: #5db52b;
    --tick-light: #9be066;
    --button-a: #5aa3b0;
    --button-b: #2f7d8c;
    --footer: #8a8f99;
  }
  * { box-sizing: border-box; margin: 0; padding: 0; }
  html, body { width: 1200px; height: 1152px; overflow: hidden; }
  body {
    position: relative;
    font-family: "Arimo", Arial, sans-serif;
    color: var(--text);
    background:
      linear-gradient(180deg, var(--bg-top) 0, var(--bg-top-edge) 355px, var(--bg-bottom-a) 356px, var(--bg-bottom-b) 1152px);
  }
  .abs { position: absolute; }
  .card {
    left: 149px; top: 128px; width: 903px; height: 950px;
    background: var(--card);
    box-shadow: 0 2px 8px rgba(60, 80, 110, .18);
  }
  .brand-name {
    left: 178px; top: 38px;
    font-size: 56px; font-weight: 700; color: var(--teal-dark);
    line-height: 1; letter-spacing: -1px;
  }
  .header-band {
    left: 149px; top: 96px; width: 903px; height: 32px;
    background: var(--teal-dark);
  }
  .header-tagline {
    left: 427px; top: 101px;
    font-size: 17px; font-weight: 700; color: #fff; letter-spacing: .6px;
  }
  .quality-badge {
    left: 922px; top: 23px; width: 105px; height: 123px;
    background: linear-gradient(180deg, #f4f6f7 0, #e4eaec 60%, #7fa9b3 61%, #5a8f9b 100%);
    border: 1px solid #c9d2d6;
    box-shadow: 0 2px 5px rgba(0,0,0,.25);
  }
  .headline {
    left: 188px; top: 148px;
    font-size: 22px; font-weight: 700; color: var(--teal-text);
  }
  .rule { left: 188px; width: 820px; height: 1px; background: var(--rule); }
  .photo-woman {
    left: 252px; top: 240px; width: 266px; height: 368px;
    background: radial-gradient(ellipse at 40% 45%, #3a2a24 0, #1b1717 45%, #f4efec 72%, #ffffff 100%);
    border-radius: 10px;
  }
  .benefits { left: 546px; top: 288px; list-style: none; }
  .benefits li {
    display: flex; align-items: center; height: 49.5px;
    font-size: 19.5px;
  }
  .benefits svg { width: 36px; height: 36px; margin-right: 29px; flex: none; }
  .stamp {
    left: 815px; top: 511px; width: 175px; height: 123px;
    background: radial-gradient(circle at 55% 55%, #6b6b6b 0, #9c9c9c 38%, #e6e6e6 58%, #ffffff 75%);
  }
  .intro { left: 190px; top: 690px; width: 480px; }
  .intro h2 {
    font-size: 17.5px; font-weight: 700; color: var(--teal-text);
    line-height: 27px;
  }
  .intro p { font-size: 17.5px; line-height: 27.5px; white-space: nowrap; }
  .intro .block + .block { margin-top: 22px; }
  .photo-team {
    left: 683px; top: 667px; width: 340px; height: 265px;
    background: linear-gradient(90deg, #f2f2f2 0, #d9d2c8 35%, #b8a58a 62%, #e7e4df 85%, #fafafa 100%);
  }
  .cta {
    left: 388px; top: 984px; width: 492px; height: 48px;
    background: linear-gradient(180deg, var(--button-a), var(--button-b));
    border: 1px solid #2a6c79;
    color: #fff; font-size: 19.5px; font-weight: 700;
    display: flex; align-items: center; padding-left: 18px;
    text-shadow: 0 1px 1px rgba(0,0,0,.35);
  }
  .ssl-seal { left: 306px; top: 961px; width: 92px; height: 92px; }
  .footer-note { top: 1097px; font-size: 13px; color: var(--footer); }
  .footer-left { left: 175px; }
  .footer-right { right: 190px; }
</style>
</head>
<body>
  <div class="abs card"></div>

  <div class="abs brand-name">Alu-Kasse</div>
  <div class="abs header-band"></div>
  <div class="abs header-tagline">KREDIT - seit 35 Jahren</div>
  <div class="abs quality-badge" role="img" aria-label="Qualitätssiegel"></div>

  <h1 class="abs headline">Umfangreicher Kreditvergleich - kostenlos, schnell und fair</h1>
  <div class="abs rule" style="top:186px"></div>

  <div class="abs photo-woman" role="img" aria-label="Foto: lächelnde Frau im Blazer zeigt auf die Vorteile"></div>

  <ul class="abs benefits">
    <li><svg viewBox="0 0 36 36"><path d="M3 19 L9 14 L15 21 L30 3 L34 7 L15 33 Z" fill="var(--tick)"/><path d="M9 14 L15 21 L30 3 L32 5 L15 26 Z" fill="var(--tick-light)"/></svg>Bestes Kreditangebot von 20 Banken</li>
    <li><svg viewBox="0 0 36 36"><path d="M3 19 L9 14 L15 21 L30 3 L34 7 L15 33 Z" fill="var(--tick)"/><path d="M9 14 L15 21 L30 3 L32 5 L15 26 Z" fill="var(--tick-light)"/></svg>kostenlos und unverbindlich</li>
    <li><svg viewBox="0 0 36 36"><path d="M3 19 L9 14 L15 21 L30 3 L34 7 L15 33 Z" fill="var(--tick)"/><path d="M9 14 L15 21 L30 3 L32 5 L15 26 Z" fill="var(--tick-light)"/></svg>schnelle Bearbeitung</li>
    <li><svg viewBox="0 0 36 36"><path d="M3 19 L9 14 L15 21 L30 3 L34 7 L15 33 Z" fill="var(--tick)"/><path d="M9 14 L15 21 L30 3 L32 5 L15 26 Z" fill="var(--tick-light)"/></svg>auch Kredite ohne Kredaxa</li>
    <li><svg viewBox="0 0 36 36"><path d="M3 19 L9 14 L15 21 L30 3 L34 7 L15 33 Z" fill="var(--tick)"/><path d="M9 14 L15 21 L30 3 L32 5 L15 26 Z" fill="var(--tick-light)"/></svg>Flexible Laufzeiten</li>
  </ul>

  <div class="abs stamp" role="img" aria-label="Stempel: Kredit genehmigt"></div>
  <div class="abs rule" style="top:639px"></div>

  <section class="abs intro">
    <div class="block">
      <h2>Sparen Sie Zeit und Geld!</h2>
      <p>Ein Antrag genügt. Wir verhandeln für Sie mit 20 Banken<br>und präsentieren Ihnen das beste Kreditangebot.<br>Bequemer geht es nicht.</p>
    </div>
    <div class="block">
      <h2>Garantiert kostenlos und unverbindlich</h2>
      <p>Sie bezahlen für unseren Service keinen Cent. Auch wenn<br>Ihre Kreditanfrage abgelehnt werden sollte oder Sie es nicht<br>annehmen möchten.</p>
    </div>
  </section>

  <div class="abs photo-team" role="img" aria-label="Foto: junger Mann im Sakko vor einer Gruppe von Menschen"></div>

  <a class="abs cta">Jetzt unverbindliches Kreditangebot anfordern!</a>
  <svg class="abs ssl-seal" viewBox="0 0 92 92" role="img" aria-label="Sicherheitssiegel">
    <circle cx="46" cy="46" r="45" fill="#e2b23a"/>
    <circle cx="46" cy="46" r="30" fill="#2f5d88"/>
  </svg>

  <div class="abs footer-note footer-left">Wird dieser Newsletter falsch angezeigt? Hier melden</div>
  <div class="abs footer-note footer-right">www.alu-kasse-muster.de</div>
</body>
</html>
```